New Karvenna Business Cards with new logo

Need to keep the Logo of the guys in the boat, or new logo with guys in a boat that symbolizes the three different Alaska natives that represent the region. Would like to have in font "An Alaska Village Corporation". Business cards should include logo, and be professional. knri.com is the company website that we are looking at redesigning also.

Target Market(s)

Business Contact

Industry/Entity Type

Business

Contact Information for Business Card

Would like Name, title, address, two phone numbers Cell and direct, email.

Logo Text

Logo does not have to have text,

Font styles to use
Serif
Sans Serif

Colors

Designer to choose colors to be used in the design.

Requirements
Must have
• An Alaska Native Village Corporation; Karvenna Heritage Collective Inc. (company name)

```html
<!DOCTYPE html>
<html lang="en">
<head>
<meta charset="utf-8">
<title>Karvenna Heritage Collective – Business Card</title>
<link rel="stylesheet" href="https://fonts.googleapis.com/css2?family=Open+Sans:wght@400;600;700&display=swap">
<style>
  :root {
    --backdrop: #3a3b3d;
    --card: #ffffff;
    --teal: #1b7f8c;
    --ink: #4a4a4a;
    --navy: #25306b;
  }
  * { margin: 0; padding: 0; box-sizing: border-box; }
  html, body {
    width: 1200px; height: 1000px; overflow: hidden;
    background: var(--backdrop);
    font-family: "Open Sans", Arial, sans-serif;
  }
  .card {
    position: absolute;
    left: 100px; top: 214px;
    width: 1000px; height: 572px;
    background: var(--card);
    box-shadow: 0 18px 40px rgba(0,0,0,0.45);
  }
  .brand {
    position: absolute;
    right: 90px; top: 70px;
    display: flex; align-items: center; gap: 14px;
  }
  .brand-mark {
    width: 22px; height: 22px; border-radius: 50%;
    background: var(--navy);
  }
  .brand-name {
    font-weight: 700; font-size: 22px; line-height: 1.25;
    color: var(--navy); letter-spacing: 0.5px;
    text-transform: uppercase; text-align: left;
  }
  .divider {
    position: absolute;
    left: 58px; right: 58px; top: 318px;
    height: 2px; background: var(--teal);
  }
  .person {
    position: absolute; left: 58px; top: 216px;
  }
  .person-name {
    font-size: 44px; font-weight: 600; color: var(--teal); line-height: 1.1;
  }
  .person-title {
    font-size: 26px; color: var(--ink); line-height: 1.2; margin-left: 14px;
  }
  .contacts {
    position: absolute; left: 70px; top: 336px;
    list-style: none;
  }
  .contacts li {
    display: flex; align-items: center; gap: 18px;
    font-size: 27px; color: var(--ink); line-height: 40px;
  }
  .contacts svg { width: 20px; height: 20px; fill: var(--teal); flex: none; }
  .contacts .accent { color: var(--teal); }
  .org {
    position: absolute; right: 58px; top: 338px; text-align: right;
  }
  .org-tagline {
    font-size: 25px; font-weight: 700; color: var(--teal);
    letter-spacing: 0.3px; text-transform: uppercase;
  }
  .org-address {
    font-size: 24px; color: var(--ink); line-height: 1.3; margin-top: 4px;
  }
</style>
</head>
<body>
  <article class="card">
    <div class="brand">
      <span class="brand-mark"></span>
      <div class="brand-name">Karvenna Heritage<br>Collective, Inc.</div>
    </div>

    <div class="person">
      <div class="person-name">Michel Smith</div>
      <div class="person-title">Owner</div>
    </div>

    <div class="divider"></div>

    <ul class="contacts">
      <li>
        <svg viewBox="0 0 20 20"><path d="M6 1h8a1.5 1.5 0 0 1 1.5 1.5v15A1.5 1.5 0 0 1 14 19H6a1.5 1.5 0 0 1-1.5-1.5v-15A1.5 1.5 0 0 1 6 1zm.5 2v12h7V3zm3.5 13.2a1 1 0 1 0 0 2 1 1 0 0 0 0-2z"/></svg>
        000 112 2229
      </li>
      <li>
        <svg viewBox="0 0 20 20"><path d="M5 1.5l3 3.5-1.6 2.2c.9 2.2 2.7 4.1 4.9 5.2L13.5 11l3.5 3-1.8 3.4C9 17 3 10.6 2.3 4.4z"/></svg>
        000 111 2224
      </li>
      <li>
        <svg viewBox="0 0 20 20"><path d="M1 4h18v1.2l-9 6-9-6zm0 3.2l9 6 9-6V16H1z"/></svg>
        urname@email.com
      </li>
      <li>
        <svg viewBox="0 0 20 20"><path d="M10 1a9 9 0 1 0 0 18 9 9 0 0 0 0-18zm0 1.6c.9 0 2 1.8 2.4 4.4H7.6C8 4.4 9.1 2.6 10 2.6zM6 7H3.1a7.4 7.4 0 0 1 4-3.8C6.6 4.3 6.2 5.6 6 7zm8 0c-.2-1.4-.6-2.7-1.1-3.8a7.4 7.4 0 0 1 4 3.8zM2.7 8.6H6v2.8H2.7a7.4 7.4 0 0 1 0-2.8zm4.9 0h4.8v2.8H7.6zm6.4 0h3.3a7.4 7.4 0 0 1 0 2.8H14zM3.1 13H6c.2 1.4.6 2.7 1.1 3.8a7.4 7.4 0 0 1-4-3.8zm4.5 0h4.8c-.4 2.6-1.5 4.4-2.4 4.4S8 15.6 7.6 13zm6.4 0h2.9a7.4 7.4 0 0 1-4 3.8c.5-1.1.9-2.4 1.1-3.8z"/></svg>
        <span>www.<span class="accent">knri</span>.com</span>
      </li>
    </ul>

    <div class="org">
      <div class="org-tagline">An Alaska Village Corporation</div>
      <div class="org-address">Your Street Address,<br>alaska, 1234</div>
    </div>
  </article>
</body>
</html>
```